Anzeigengestaltung für Bernstein Ankaufstage in Wien
Zielgruppe
Zweck dieser Anzeige ist:
sowiele Leute wie möglich zu überzeugen, mit Ihrem Bernstein, zu uns in die Ankaufsaktion zu kommen.
Wer wir sind:
Wir sind eine Firma aus Deutschland, die sich auf die Bewertung und den Ankauf von Bernstein (Rohbernstein, Bernsteinschmuck, Kunstobjekte aus Bernstein etc. ) spezialisiert hat.
Wir führen in verschiedenen Städten Aktionen durch, in denen wir Bernstein bewerten und ggf. auch ankaufen.
Zielgruppe:
Alle leser einer Tageszeitung, Alter 50 + überwiegend ältere Damen, und generel Haushalte die Bernstein besitzen
siehe Bsp. Anzeige Wien (Datei upload)
Aufgabenstellung
Anzeigengröße B 198 mm x H 270 mm
Technische Angaben siehe PDF Tageszeitungproduktion (Datei upload)
Wir wollen auf jedenfall eine Anzeige die auch effektreich ist, nicht nur 2-dimensional und platt bleibt, sondern auch verschiedene Tiefen hat. Aber sie soll trotzdem plakativ sein.
Die Anzeige muss Seriös, Auffälig, gut lesbar, edel, frisch,..... AKTION!!
Zielgruppe ansprechen
Direkt erkennbar sein was die Anzeige bezwecken soll
Unser Hauptinteresse liegt auf den gelben ketten, davon haben wir auch 2 Bilder beigefügt.
Das wichtigste Bild ist Bild: "bernstein_2.jpg", dieses sollte schon irgendwo groß auftauchen.
Das soll auf die Anzeige:
- Textteil wie Beispielsdatei.
- AKTION
- Was....Bernstein Ankaufs-Tage in Wien
- Bernstein-Wertschätzung und Ankauf in Wien
- Wann.....vom 03.08.2017-05.08.2017
- Uhrzeit von 10:00 Uhr bis 17:00 Uhr
- Wo.... Hotel Lindenhof Palais, Mohnfeldgasse 14, 1010 Wien, Raum: Salon 3
- Was Kaufen Wir....... Bernsteinschmuck, Bernsteinketten, Bernsteinobjekte, Rohbernsteine ab 10 g,
Bernstein Kunstgegenstände.
- Wir bieten Ihnen eine kostenlose Wertschätzung Ihrer Bernsteinstücke sowie einen
Bar-Ankauf vor Ort.
- Unser Logo
- Unsere Website www.zirkel-kauf.example
- rechts oben in der Anzeige muss das Wort -ANZEIGE- in klein stehen.
Vermerk, Achtung !!! wir kaufen nur unbehandelten Naturbernstein!!!!
siehe Bsp. Anzeige Wien bei (Datei upload)

```html
<!DOCTYPE html>
<html lang="de">
<head>
<meta charset="utf-8">
<title>Bernstein Ankaufs-Tage in Wien – Anzeige</title>
<link rel="stylesheet" href="https://fonts.googleapis.com/css2?family=Abril+Fatface&family=Exo+2:wght@500&family=Open+Sans:wght@400&family=Oswald:wght@300;400;500;600&display=swap">
<style>
  :root {
    --amber: #f9b122;
    --amber-deep: #e8901a;
    --amber-light: #fcd36a;
    --ink: #141414;
    --body-ink: #3a3226;
    --slate: #3f3f41;
    --paper: #ffffff;
  }
  html, body { margin: 0; padding: 0; overflow: hidden; background: var(--paper); }
  .ad {
    position: relative;
    width: 880px; height: 1200px;
    overflow: hidden;
    background: var(--paper);
    font-family: "Open Sans", Arial, sans-serif;
  }
  .ad > * { position: absolute; }

  .panel-left { left: 0; top: 0; width: 532px; height: 1200px; background: var(--amber); }

  /* photo areas */
  .photo { margin: 0; }
  .photo-hero {
    left: 250px; top: 256px; width: 630px; height: 345px;
    background:
      radial-gradient(ellipse 28% 40% at 52% 55%, #fbc53c 0%, #f3a11f 55%, rgba(243,161,31,0) 100%),
      radial-gradient(ellipse 22% 30% at 78% 35%, #f7b32c 0%, rgba(236,140,30,0) 100%),
      radial-gradient(ellipse 60% 70% at 60% 50%, rgba(222,120,28,.85) 0%, rgba(249,177,34,0) 100%);
    -webkit-mask-image: linear-gradient(to right, rgba(0,0,0,.35) 0%, #000 45%);
    mask-image: linear-gradient(to right, rgba(0,0,0,.35) 0%, #000 45%);
  }
  .photo-bracelet {
    left: 532px; top: 598px; width: 348px; height: 250px;
    background:
      radial-gradient(ellipse 40% 45% at 72% 50%, #fbc94a 0%, rgba(251,201,74,0) 100%),
      radial-gradient(ellipse 30% 35% at 35% 75%, #d9701a 0%, rgba(217,112,26,0) 100%),
      radial-gradient(ellipse 75% 60% at 50% 50%, #f0a42a 0%, rgba(255,255,255,0) 100%);
  }
  .photo-pendants {
    left: 532px; top: 867px; width: 306px; height: 164px;
    background:
      radial-gradient(ellipse 25% 45% at 22% 65%, #c9601a 0%, rgba(201,96,26,0) 100%),
      radial-gradient(ellipse 70% 60% at 55% 55%, #f2a42c 0%, rgba(255,255,255,0) 100%);
  }

  .tag-anzeige {
    right: 58px; top: 16px;
    font-family: "Oswald", Arial, sans-serif; font-weight: 400;
    font-size: 11px; letter-spacing: 2px; color: var(--slate);
  }

  /* brand */
  .brand { left: 580px; top: 58px; width: 230px; text-align: center; }
  .brand-dot {
    display: block; margin: 0 auto 12px;
    width: 46px; height: 46px; border-radius: 50%;
    background: var(--amber);
  }
  .brand-name {
    font-family: "Oswald", Arial, sans-serif; font-weight: 400;
    font-size: 26px; letter-spacing: 3px; color: var(--slate); line-height: 1;
  }

  .aktion {
    left: 591px; top: 157px; width: 207px;
    border-top: 5px solid var(--amber); border-bottom: 5px solid var(--amber);
    text-align: center;
    font-family: "Oswald", Arial, sans-serif; font-weight: 500;
    font-size: 74px; line-height: 86px; letter-spacing: 0; color: var(--slate);
    padding: 2px 0;
  }

  .headline {
    left: 62px; top: 78px; margin: 0;
    font-family: "Abril Fatface", Georgia, serif; font-weight: 400;
    font-size: 60px; line-height: 63px; color: var(--ink);
  }

  .offer {
    left: 115px; top: 282px; width: 340px; margin: 0;
    font-family: "Abril Fatface", Georgia, serif;
    font-size: 12.5px; line-height: 25px; color: var(--ink);
  }
  .offer-lead { font-size: 20px; }

  .story { left: 54px; width: 438px; margin: 0; }
  .story h2 {
    margin: 0 0 1px;
    font-family: "Exo 2", Arial, sans-serif; font-weight: 500;
    font-size: 19px; line-height: 22px; color: var(--paper);
  }
  .story p {
    margin: 0;
    font-size: 11.2px; line-height: 17.2px; color: var(--body-ink);
    text-align: justify; hyphens: auto;
  }
  .story-1 { top: 437px; }
  .story-2 { top: 615px; }
  .story-3 { top: 793px; }

  .website {
    left: 54px; top: 1102px; width: 438px; text-align: center;
    font-family: "Oswald", Arial, sans-serif; font-weight: 500;
    font-size: 17px; color: var(--paper); letter-spacing: .3px;
  }
  .notice {
    left: 54px; top: 1130px; width: 438px; margin: 0;
    border-top: 1.5px solid var(--ink); border-bottom: 1.5px solid var(--ink);
    font-family: "Oswald", Arial, sans-serif; font-weight: 300;
    font-size: 16.5px; line-height: 27px; color: var(--ink);
    text-transform: uppercase; white-space: nowrap;
  }

  .event {
    left: 560px; top: 1056px; width: 280px; margin: 0;
    text-align: center; font-style: normal;
    font-family: "Oswald", Arial, sans-serif; color: var(--slate);
    text-transform: uppercase;
  }
  .event span { display: block; }
  .event-date { font-size: 15px; line-height: 26px; font-weight: 300; }
  .event-date b, .event-phone b { font-weight: 500; font-size: 18px; }
  .event-phone { font-size: 15px; line-height: 24px; font-weight: 300; }
  .event-venue { font-size: 17px; line-height: 26px; font-weight: 500; }
  .event-address { font-size: 13.5px; line-height: 26px; font-weight: 300; white-space: nowrap; }

  .foot-bar { left: 580px; top: 1165px; width: 246px; height: 35px; background: var(--amber); }
</style>
</head>
<body>
<main class="ad">
  <div class="panel-left"></div>

  <figure class="photo photo-hero" role="img" aria-label="Foto: große gelbe Honigbernstein-Ketten mit runden und ovalen Perlen"></figure>
  <figure class="photo photo-bracelet" role="img" aria-label="Foto: Bernsteinarmband, Ketten und silbergefasste Bernsteinanhänger"></figure>
  <figure class="photo photo-pendants" role="img" aria-label="Foto: Bernsteinketten mit Anhängern und Brosche"></figure>

  <div class="tag-anzeige">ANZEIGE</div>

  <div class="brand">
    <span class="brand-dot"></span>
    <div class="brand-name">LUMERA</div>
  </div>

  <div class="aktion">AKTION</div>

  <h1 class="headline">Bernstein<br>Ankaufs-Tage<br>in Wien</h1>

  <p class="offer"><span class="offer-lead">Was Kaufen Wir:</span> Bernsteinschmuck, Bernsteinketten, Bernsteinobjekte, Rohbernsteine ab 10 g, Bernstein Kunstgegenstände. Wir bieten Ihnen eine kostenlose Wertschätzung Ihrer Bernsteinstücke sowie einen Bar-Ankauf vor Ort.</p>

  <section class="story story-1">
    <h2>Vergessene Schätze</h2>
    <p>Einst als kostbare Fracht entlang der Bernsteinstraße (östliche römische Route) gelangte Bernstein von der Nord- und Ostsee nach Süden in den Mittelmeerraum. Gezeichnet durch kunstvoll gefertigte Gegenstände und allerlei Schmuck rühmt sich das fossile Harz einer langen und vielfältigen Geschichte. Doch diese facettenreiche Geschichte scheint heute für die meisten in Vergessenheit geraten zu sein und klingt bestenfalls noch wie ein Märchen aus der Kindheit. Oft sogar als „langweilig“ oder „aus der Mode gekommen“ gebrandmarkt, wurde der Naturbernstein hier zunehmend von Juwelier-Schaufenstern und Vitrinen verbannt.</p>
  </section>

  <section class="story story-2">
    <h2>Ein neues Kapitel</h2>
    <p>Nichtsdestoweniger wird dem Bernstein heute weltweit mehr Wertschätzung gezollt als je zuvor. Seit Neuestem wurde ein neues Kapitel aufgeschlagen. Die Bernsteinstraße, die einst gen Süden ging, führt heute bis nach China im Fernen Osten. Die aktuelle Nachfrage aus Asien hat den Handel mit Bernstein auf ganz neue Weise wiederbelebt und den Preis teilweise beträchtlich ansteigen lassen. Was mitunter in Wiener Haushalten seit Jahrzehnten in Schmuckkästchen verstaubt, wird in China als begehrtes Schmuckstück teuer gehandelt. Dort gilt Bernstein unter anderem als Symbol des Reichtums und wird stolz in der Öffentlichkeit getragen.</p>
  </section>

  <section class="story story-3">
    <h2>Große Werte</h2>
    <p>Die Wertbestimmung für Bernstein hat sich jedoch gewandelt und abhängig von bestimmten Merkmalen variiert der Preis sehr stark. Der hier sonst sehr übliche cognacfarbene und transparente Bernsteinschmuck ist kaum mehr gefragt und in jeglicher Form behandelter oder gepresster Bernstein findet so gut wie keine Beachtung mehr. Dahingegen dominiert heute vor allem der unbehandelte naturbelassene Honigbernstein den Handel. Gelb bis orangefarbene milchige in Oliven- oder Kugelform gefertigte Ketten sind die absoluten Renner. Antike Bernsteinketten, die durch Verwitterung im Laufe der Jahre unterschiedlich stark rot bis rotbraun gefärbt wurden, sind besonders interessant. Auch sonstige Schmuckstücke, wie etwa Armbänder, Anhänger, Ringe, Broschen und andere Kleingegenstände sind beliebt. Das gilt auch für Schmuckschatullen, Schnitzereien und Kunstgegenstände aus Natur-Bernstein. Zum einen ist natürlich das Alter und der Zustand für den Preis entscheidend, aber auch Dinge wie Farbe, Größe und Marmorierung sind wichtige Faktoren. Sammler bevorzugen überwiegend gut erhaltene und antike Stücke. Es empfiehlt sich in jedem Fall einen geeigneten Fachmann zu Rate zu ziehen.</p>
  </section>

  <div class="website">WWW.ZIRKEL-KAUF.EXAMPLE</div>
  <p class="notice">Vermerk, Achtung !!! Wir kaufen nur unbehandelten Naturbernstein!</p>

  <address class="event">
    <span class="event-date">Vom <b>03.08.2017 - 05.08.2017</b></span>
    <span class="event-phone">Telefon: <b>+43 600 51829370</b></span>
    <span class="event-venue">Hotel Lindenhof Palais,</span>
    <span class="event-address">Mohnfeldgasse 14, 1010 Wien, Raum: Salon 3</span>
  </address>

  <div class="foot-bar"></div>
</main>
</body>
</html>
```